Vocational Mentor needs an impressive business card

1. I need a business card (or maybe three with identic look) to promote me and my three business titles/services:
- Vocational Mentor. I help people find their vocation and live happily from it. I use my 20 years of experience in business, management and psychology to help them identify the most efficient ways to make a living doing what they are passionate about.
- Business Angel. I help founders start a succesful business with minimum risks and costs. I use my 20 years of experience in sales, management and entrepreneurship to help them identify the most efficient ways, in terms of time and cost, to validate their business idea.
- Learning Designer. I design unique learning programs that produce long-term cognitive and behavioural changes to people and organisations. I use my 20 years of experience in learning, teaching and change management to create minimalist experiences and processes that allow them to change efficiently in their pursued direction.

2. I would like a two-sided business card, on the front with my name, contact details and titles, on the back the explanation of the services.
Updates

Hi all,

I updated my brief, included contacts info and give feedback on all designs I got. I am new on this platform so please tell me if you need anything else or if I don't use corectly the platform forms.

Kind regards,
Mirel

Hi all,

I shortened the services description by deleting the phrase "I call..."

Kind regards,
Mirel

Target Market(s)

Freelancers, startups, people and organization willing to invest in change through ultimate learning experiences

Industry/Entity Type

Business

Font styles to use
Serif

Requirements
Must have
• Front side: full name, titles, web site, email, phone like below:
Mirel Vantaru
Vocational Mentor, Business Angel, Learning Designer
info@mirelvantaru.example
www.mirelvantaru.example
+40-748-MIRELV
Nice to have
• Back side: the description of the services I provide as in the task description.
1/3: it would be nice if I can jam all three titles on the front side but then I need a solution to jam all three services on the back side.

```html
<!DOCTYPE html>
<html lang="en">
<head>
<meta charset="utf-8">
<title>Mirel Vantaru – Business Card</title>
<link rel="stylesheet" href="https://fonts.googleapis.com/css2?family=Arimo:wght@400;700&display=swap">
<style>
  :root {
    --teal: #0ca6cc;
    --orange: #e8601e;
    --white: #ffffff;
    --paper: #ffffff;
  }
  * { margin: 0; padding: 0; box-sizing: border-box; }
  html, body {
    width: 933px;
    height: 1200px;
    overflow: hidden;
    background: var(--paper);
    font-family: "Arimo", Arial, sans-serif;
  }
  .canvas { position: relative; width: 933px; height: 1200px; }

  /* Front side */
  .card-front {
    position: absolute; left: 0; top: 0;
    width: 933px; height: 564px;
    background: var(--teal);
  }
  .name-band {
    position: absolute; left: 0; top: 113px;
    width: 100%; height: 130px;
    background: var(--white);
  }
  .accent-bar {
    position: absolute; left: 45px; top: 57px;
    width: 12px; height: 469px;
    background: var(--orange);
  }
  .name {
    position: absolute; left: 88px; top: 124px;
    font-size: 50px; font-weight: 700; line-height: 1;
    color: var(--teal);
    letter-spacing: 0.3px;
  }
  .name .surname { color: var(--orange); }
  .titles {
    position: absolute; left: 88px; top: 197px;
    font-size: 26px; line-height: 1;
    color: var(--teal);
  }
  .contact {
    position: absolute; left: 0; width: 100%;
    color: var(--white); font-size: 28px; line-height: 1;
  }
  .contact-web-mail { top: 459px; }
  .contact-web-mail .web { position: absolute; left: 120px; }
  .contact-web-mail .mail { position: absolute; left: 509px; }
  .contact-phone { top: 508px; text-align: center; padding-left: 30px; }

  /* Back side */
  .card-back {
    position: absolute; left: 0; top: 635px;
    width: 933px; height: 565px;
    background: var(--teal);
  }
  .edge-line {
    position: absolute; top: 0; height: 100%;
    width: 6px; background: var(--orange);
  }
  .edge-line.one { left: 897px; }
  .edge-line.two { left: 907px; }
  .service {
    position: absolute; left: 30px; width: 856px;
    color: var(--white);
    font-size: 24.3px; line-height: 27.6px;
  }
  .service.mentor { top: 58px; }
  .service.angel { top: 225px; }
  .service.designer { top: 373px; text-align: justify; }
</style>
</head>
<body>
<main class="canvas">
  <section class="card-front" aria-label="Front side">
    <div class="name-band"></div>
    <div class="accent-bar"></div>
    <h1 class="name">Mirel <span class="surname">Vantaru</span></h1>
    <p class="titles">Vocational Mentor, Business Angel, Learning Designer</p>
    <p class="contact contact-web-mail">
      <span class="web">www.mirelvantaru.example</span>
      <span class="mail">info@mirelvantaru.example</span>
    </p>
    <p class="contact contact-phone">+40-748-MIRELV</p>
  </section>

  <section class="card-back" aria-label="Back side">
    <div class="edge-line one"></div>
    <div class="edge-line two"></div>
    <p class="service mentor">- Vocational Mentor. I help people to find their vocation and live happily from it. I use my 20 years of experience in business, management and psychology to help them identify the most efficient ways to make a living doing what they are passionate about.</p>
    <p class="service angel">- Business Angel. I help founders to start a succesful business with minimum risks and costs. I use my 20 years of experience in sales, management and entrepreneurship to help them identify the most efficient ways, in terms of time and cost, to validate their business idea.</p>
    <p class="service designer">- Learning Designer. I design unique learning programs that produce long-term cognitive and behavioural changes to people and organisations. I use my 20 years of experience in learning, teaching and change management to create minimalist experiences and processes that allows them to change efficiently in their pursued direction.</p>
  </section>
</main>
</body>
</html>
```